Brand New Church Business Card Design. Needs to appeal to high school students, professionals.

Business Card. Bold lines and colors. Simple font. This is a new church looking to attract new families who have moved to the area. Business professionals mostly. have a working logo. may need a little tweaking. Church is designed to do excellent ministries for students and children. Like business card design in box on mark vault homepage. Want a front and back side. Prefer colors to match the logo. But will lean on designers preferences and wisdom. DO NOT WANT A CROSS OR RELIGIOUS SYMBOL on the card.

Target Market(s)

Families, Professionals, Students

Industry/Entity Type

High School

Contact Information for Business Card

SaltRock ChurchSaltRock.atForrest Coulter904-515-8349Forrest@PineHollow.at

Font styles to use
Sans Serif

Colors
0255a3
ffffff

Requirements
Must have
• Bold colors. Very Masculine. Creative
Nice to have
• On printnook.markvault.com homepage in the business card design box. the card with the black, blue and gray looks really sharp. matches our logos.
Should not have
• no crosses or religious symbols.

```html
<!DOCTYPE html>
<html lang="en">
<head>
<meta charset="utf-8">
<title>PineHollow Church – Business Card</title>
<link rel="stylesheet" href="https://fonts.googleapis.com/css2?family=Arimo:wght@400;700&display=swap">
<style>
  :root {
    --sky: #12a8f8;
    --sky-light: #5cc6fc;
    --mist: #eef2f5;
    --glow: #9fd8fb;
    --deep: #0255a3;
    --white: #ffffff;
    --ink: #000000;
    --font: "Arimo", Arial, sans-serif;
  }
  html, body {
    margin: 0;
    padding: 0;
    overflow: hidden;
    background: var(--white);
  }
  .canvas {
    position: relative;
    width: 973px;
    height: 1200px;
    overflow: hidden;
    font-family: var(--font);
    background: var(--white);
  }
  .card {
    position: absolute;
    left: 0;
    width: 973px;
    background: var(--sky);
    overflow: hidden;
  }
  .card--front { top: 0; height: 570px; }
  .card--back { top: 630px; height: 570px; }

  .header-art {
    position: absolute;
    left: 0;
    top: 0;
    width: 973px;
    height: 340px;
    background: linear-gradient(160deg, var(--mist) 0%, var(--glow) 40%, var(--sky) 85%);
  }
  .brand {
    position: absolute;
    left: 46px;
    top: 98px;
    display: flex;
    align-items: center;
    gap: 14px;
  }
  .brand__dot {
    width: 44px;
    height: 44px;
    border-radius: 50%;
    background: var(--sky);
  }
  .brand__name {
    font-size: 36px;
    font-weight: 700;
    color: var(--white);
    line-height: 1;
  }
  .values {
    position: absolute;
    left: 380px;
    top: 364px;
    margin: 0;
    padding: 0;
    list-style: none;
    color: var(--white);
    font-size: 41px;
    line-height: 46px;
  }
  .contact-title {
    position: absolute;
    left: 439px;
    top: 242px;
    margin: 0;
    color: var(--white);
    font-size: 36px;
    font-weight: 400;
    line-height: 40px;
  }
  .contact-box {
    position: absolute;
    left: 541px;
    top: 294px;
    width: 400px;
    height: 230px;
    box-sizing: border-box;
    padding: 12px 0 0 28px;
    background: var(--sky-light);
    color: var(--ink);
    font-size: 34px;
    line-height: 41.7px;
    font-style: normal;
    white-space: nowrap;
  }
</style>
</head>
<body>
<div class="canvas">
  <section class="card card--front">
    <div class="header-art" role="img" aria-label="Decorative sweeping blue wave artwork across the top of the card"></div>
    <div class="brand">
      <span class="brand__dot"></span>
      <span class="brand__name">PineHollow Church</span>
    </div>
    <ul class="values">
      <li>Courageous Faith</li>
      <li>Next Generation Excellence</li>
      <li>Serving Big</li>
    </ul>
  </section>

  <section class="card card--back">
    <h2 class="contact-title">Contact Us :</h2>
    <address class="contact-box">
      PineHollow Church<br>
      PineHollow.at<br>
      Dwayne Pellish<br>
      904-555-0172<br>
      Dwayne@PineHollow.at
    </address>
  </section>
</div>
</body>
</html>
```